Website for company called VELQUOgen

We need a website for our new company called VELQUOgen which developed a platform/technology to identify antigen-specific T cells (immune cells) which can be used for cancer therapy, autoimmunity, etc.

The platform is called VELQUO and is rapid, versatile, unbiased, and inexpensive.

We have a semi-final logo although we are not completely set on color and font of text (attached).

Target Market(s)

Our target audience at the moment would be potential investors and VCs. We eventually are interested in getting attention from scientists and cell/immunotherapy companies.

Industry/Entity Type

Healthcare/Technology

Coding

Coded - Design and coding required

Number of Pages Required

1 page

Colors
0094D4
00A9DD
6FCCEA
C7EBF8
E9F6FB
00AB8E
00BBA5
67D7C9
C6EFE9
E9F9F6
E54698
E96AAD
F1A4CE
F9D9EA
FCEFF6
A7469A
B969AE
D3A5CF
EDDBEB
F8F0F9
6B429C
8869AF
B7A5CE
E3DAEB
F3F0F8

Requirements
Must have
• Landing page about the company, About us page, Technology page (could be merged with company landing page), Contact us page

```html
<!DOCTYPE html>
<html lang="en">
<head>
<meta charset="utf-8">
<title>VELQUOgen — Identifying antigen-specific T cells</title>
<link href="https://fonts.googleapis.com/css2?family=Krona+One&family=Inter:wght@400;500;600&display=swap" rel="stylesheet">
<style>
:root{
  --blue:#00A9DD;
  --blue-deep:#0094D4;
  --teal:#00AB8E;
  --ink:#1C2227;
  --body:#4A5258;
  --bg-light:#EAF6FA;
  --white:#FFFFFF;
  --footer:#1B2529;
  --footer-text:#B9C3C8;
}
*{margin:0;padding:0;box-sizing:border-box}
html,body{width:1200px;height:4587px;overflow:hidden}
body{font-family:'Inter',sans-serif;color:var(--body);background:var(--bg-light)}
.page{position:relative;width:1200px;height:4587px;overflow:hidden}
.backdrop{position:absolute;left:0;top:0}
.display{font-family:'Krona One',sans-serif;color:var(--ink);font-weight:400}
.eyebrow{font-family:'Krona One',sans-serif;font-size:13px;color:var(--blue-deep);letter-spacing:.5px}
.section-title{font-size:42px;line-height:47px}
.para{font-size:14px;line-height:27px;color:var(--body)}

/* buttons */
.btn{display:flex;align-items:center;height:48px;background:var(--blue);color:#fff;font-size:15px;font-weight:600;border-radius:24px;padding-left:28px}
.btn .arrow{position:absolute;right:-4px;top:-4px;width:56px;height:56px;border-radius:50%;background:var(--blue);display:flex;align-items:center;justify-content:center}

/* positioning helper — declared after components so it wins */
.abs{position:absolute}

/* top bar */
.topbar{left:0;top:0;width:1200px;height:45px;background:var(--blue-deep);color:#fff;font-size:13px;display:flex;align-items:center;padding:0 85px}
.topbar .item{display:flex;align-items:center;gap:8px;margin-right:30px}
.topbar .follow{margin-left:auto;display:flex;align-items:center;gap:14px;font-weight:500}
.follow .rule{width:36px;height:1px;background:currentColor;opacity:.7}
.social-dot{width:12px;height:12px;border-radius:50%;background:currentColor;display:inline-block;margin-left:10px}

/* header */
.brand{display:flex;align-items:center;gap:10px}
.brand-mark{width:26px;height:26px;border-radius:50%;background:var(--ink)}
.brand-name{font-family:'Krona One',sans-serif;font-size:31px;color:var(--ink)}
.nav{left:608px;top:86px;display:flex;gap:36px;font-size:14px;color:var(--ink)}
.nav .active{color:var(--blue-deep)}

/* hero */
.hero-title{left:85px;top:232px;font-size:38px;line-height:61px}
.next{left:85px;top:600px;display:flex;align-items:center;gap:8px;font-family:'Krona One',sans-serif;color:var(--blue-deep);font-size:13px}
.next .count{font-size:40px;color:var(--ink);margin-left:6px}
.next .slash{font-size:26px;color:var(--ink)}

/* bullets */
.bullets{list-style:none;font-size:14px;line-height:27px;color:var(--body)}
.bullets li{position:relative;padding-left:19px;margin-bottom:9px}
.bullets li::before{content:"";position:absolute;left:0;top:10px;width:8px;height:8px;border-radius:50%;background:var(--teal)}

/* services */
.service-label{font-family:'Krona One',sans-serif;font-size:17px;fill:#fff}

/* testimonials */
.quote{width:300px;height:180px}
.quote .avatar{position:absolute;left:0;top:0;width:66px;height:66px;border-radius:50%;border:2px solid var(--blue);background:linear-gradient(#DCE6EA,#AEBFC7)}
.quote .who{position:absolute;left:80px;top:0}
.quote .name{font-family:'Krona One',sans-serif;font-size:14px;color:var(--ink)}
.quote .role{font-size:13px;color:var(--body);margin-top:4px}
.quote p{position:absolute;left:80px;top:46px;width:240px;font-size:14px;line-height:24px}
.circle-btn{width:44px;height:44px;border-radius:50%;display:flex;align-items:center;justify-content:center}

/* form */
.field{border-bottom:1px solid #B8C3C8;font-size:14px;color:var(--body);padding-bottom:12px}

/* footer */
.footer-text{color:var(--footer-text);font-size:14px;line-height:24px}
.footer-head{font-family:'Krona One',sans-serif;font-size:14px;color:#fff}
.footer-row{display:flex;align-items:flex-start;gap:8px;color:var(--footer-text);font-size:14px;line-height:22px}
.legal{top:4540px;left:85px;width:1030px;display:flex;font-size:12px;color:var(--footer-text)}
.legal .links{display:flex;gap:14px}
.legal .links .on{color:#fff;font-weight:600}
</style>
</head>
<body>
<div class="page">

  <svg class="backdrop" width="1200" height="4587" viewBox="0 0 1200 4587">
    <defs>
      <radialGradient id="heroGlow" cx="0.25" cy="0.12" r="0.6">
        <stop offset="0" stop-color="#CFEDF8"/>
        <stop offset="1" stop-color="#EEF8FB"/>
      </radialGradient>
    </defs>
    <rect x="0" y="0" width="1200" height="1000" fill="url(#heroGlow)"/>
    <path d="M0,908 C300,908 350,645 600,645 C850,645 900,908 1200,908 L1200,1184 C900,1184 850,1442 600,1442 C350,1442 300,1184 0,1184 Z" fill="#fff"/>
    <path d="M0,2065 C300,2065 350,1807 600,1807 C850,1807 900,2065 1200,2065 L1200,2643 C900,2643 850,2902 600,2902 C350,2902 300,2643 0,2643 Z" fill="#fff"/>
    <path d="M0,3525 C300,3525 350,3258 600,3258 C850,3258 900,3525 1200,3525 L1200,3907 L0,3907 Z" fill="#fff"/>
    <path d="M0,3907 C300,3907 350,4166 600,4166 C850,4166 900,3907 1200,3907 L1200,4587 L0,4587 Z" fill="var(--footer)"/>
    <g fill="none" stroke="var(--teal)" stroke-width="7">
      <path d="M0,908 C300,908 350,645 600,645 C850,645 900,908 1200,908"/>
      <path d="M0,1184 C300,1184 350,1442 600,1442 C850,1442 900,1184 1200,1184"/>
      <path d="M0,2065 C300,2065 350,1807 600,1807 C850,1807 900,2065 1200,2065"/>
      <path d="M0,2643 C300,2643 350,2902 600,2902 C850,2902 900,2643 1200,2643"/>
      <path d="M0,3525 C300,3525 350,3258 600,3258 C850,3258 900,3525 1200,3525"/>
      <path d="M0,3907 C300,3907 350,4166 600,4166 C850,4166 900,3907 1200,3907"/>
    </g>
  </svg>

  <!-- top bar -->
  <div class="abs topbar">
    <div class="item">
      <svg width="13" height="13" viewBox="0 0 24 24"><path fill="#fff" d="M6.6 10.8a15.1 15.1 0 0 0 6.6 6.6l2.2-2.2a1 1 0 0 1 1-.25 11.4 11.4 0 0 0 3.6.57 1 1 0 0 1 1 1V20a1 1 0 0 1-1 1A17 17 0 0 1 3 4a1 1 0 0 1 1-1h3.5a1 1 0 0 1 1 1c0 1.25.2 2.45.57 3.57a1 1 0 0 1-.25 1z"/></svg>
      1800-555-019
    </div>
    <div class="item">
      <svg width="14" height="11" viewBox="0 0 24 18"><rect width="24" height="18" fill="#fff"/><path d="M1 1l11 8 11-8" stroke="#0094D4" stroke-width="2" fill="none"/></svg>
      info@velquogen.com
    </div>
    <div class="follow">Follow Us <span class="rule"></span>
      <span><span class="social-dot"></span><span class="social-dot"></span><span class="social-dot"></span><span class="social-dot"></span></span>
    </div>
  </div>

  <!-- header -->
  <div class="abs brand" style="left:85px;top:76px">
    <span class="brand-mark"></span><span class="brand-name">velquogen</span>
  </div>
  <nav class="abs nav">
    <span class="active">Home</span><span>About Us</span><span>Technology</span>
  </nav>
  <div class="abs btn" style="left:911px;top:74px;width:196px;height:48px">Contact us
    <span class="arrow"><svg width="16" height="12" viewBox="0 0 16 12"><path d="M0 6h14M9 1l5 5-5 5" stroke="#fff" stroke-width="1.8" fill="none"/></svg></span>
  </div>

  <!-- hero -->
  <div class="abs eyebrow" style="left:89px;top:207px">VELQUOgen which developed</div>
  <h1 class="abs display hero-title">a technology<br>to identify<br>antigen-specific<br>T cells</h1>
  <div class="abs btn" style="left:85px;top:492px;width:200px;height:46px">Discover More
    <span class="arrow"><svg width="16" height="12" viewBox="0 0 16 12"><path d="M0 6h14M9 1l5 5-5 5" stroke="#fff" stroke-width="1.8" fill="none"/></svg></span>
  </div>
  <div class="abs next">NEXT
    <svg width="36" height="10" viewBox="0 0 36 10"><path d="M0 5h34M29 1l4 4-4 4" stroke="#0094D4" stroke-width="1.4" fill="none"/></svg>
    <span class="count">01</span><span class="slash">/</span>
    <svg width="34" height="34" viewBox="0 0 34 34" style="margin-left:18px"><circle cx="17" cy="17" r="15" stroke="#0094D4" stroke-width="2" fill="none"/><path d="M14 10l7 7-7 7" stroke="#0094D4" stroke-width="2" fill="none"/></svg>
  </div>
  <svg class="abs" style="left:632px;top:125px" width="428" height="552" viewBox="0 0 428 552" role="img" aria-label="Illustration of a magnified crimson T cell surrounded by dark orbs">
    <defs><radialGradient id="heroCell" cx=".5" cy=".45" r=".55"><stop offset="0" stop-color="#C43A5A"/><stop offset=".6" stop-color="#7A1E34"/><stop offset="1" stop-color="#1A1F29"/></radialGradient></defs>
    <ellipse cx="214" cy="276" rx="190" ry="250" fill="url(#heroCell)"/>
  </svg>

  <!-- about -->
  <svg class="abs" style="left:112px;top:822px;overflow:visible" width="452" height="404" viewBox="0 0 452 404">
    <defs><radialGradient id="aboutImg" cx=".4" cy=".4" r=".7"><stop offset="0" stop-color="#E0343B"/><stop offset="1" stop-color="#7E0F18"/></radialGradient></defs>
    <g fill="var(--teal)">
      <circle cx="158" cy="255" r="148"/>
      <circle cx="352" cy="45" r="92"/>
      <path d="M126.5,110.4 Q225.6,122.9 260.8,32.7 L371.6,134.9 Q284.4,177.1 304.7,274.8 Z"/>
    </g>
    <g role="img" aria-label="Microscope view of red blood cells and tissue" fill="url(#aboutImg)">
      <circle cx="158" cy="255" r="118"/>
      <circle cx="352" cy="45" r="62"/>
      <path d="M132.9,139.7 Q244,139.8 290.6,36.7 L365.2,105.6 Q266,160.2 274.9,270.8 Z"/>
    </g>
  </svg>
  <div class="abs eyebrow" style="left:614px;top:901px;font-size:12px">about the company</div>
  <h2 class="abs display section-title" style="left:614px;top:918px">velquogen</h2>
  <svg class="abs" style="left:614px;top:974px" width="56" height="20" viewBox="0 0 56 20"><circle cx="10" cy="10" r="9" fill="var(--teal)"/><circle cx="30" cy="10" r="9" fill="var(--teal)"/><rect x="10" y="5" width="20" height="10" fill="var(--teal)"/><circle cx="50" cy="10" r="4" fill="var(--teal)"/></svg>
  <p class="abs para" style="left:614px;top:1004px;width:480px">Lorem ipsum dolor sit amet, consectetur adipiscing elit. Nunc sem dui, sollicitudin eget condimentum lacinia, vestibulum et urna. Praesent accumsan tincidunt nulla vitae aliquet. Ut at enim egestas, tempor lectus eget, sodales sem. Nullam eleifend est nisl. Morbi fringilla quis nunc sed congue.</p>
  <div class="abs btn" style="left:614px;top:1161px;width:200px;height:48px">Read More
    <span class="arrow"><svg width="16" height="12" viewBox="0 0 16 12"><path d="M0 6h14M9 1l5 5-5 5" stroke="#fff" stroke-width="1.8" fill="none"/></svg></span>
  </div>

  <!-- why choose us -->
  <h2 class="abs display section-title" style="left:137px;top:1386px">Why<br>Choose Us</h2>
  <svg class="abs" style="left:137px;top:1491px" width="56" height="20" viewBox="0 0 56 20"><circle cx="10" cy="10" r="9" fill="var(--teal)"/><circle cx="30" cy="10" r="9" fill="var(--teal)"/><rect x="10" y="5" width="20" height="10" fill="var(--teal)"/><circle cx="50" cy="10" r="4" fill="var(--teal)"/></svg>
  <ul class="abs bullets" style="left:137px;top:1536px;width:440px">
    <li>Lorem ipsum dolor sit amet, consectetur adipiscing elit.</li>
    <li>Nunc sem dui, sollicitudin eget conntum lacinia, vestibulum et urna.</li>
    <li>Nullam eu lacus auctor nunc accumsan tempor.</li>
    <li>Aenean neque dolor, tincidunt id diam sit amet.</li>
    <li>Aliquam mattis, nunc ac maa consequat, erat dui consequat nibh, Aliquam molestie commodo.</li>
    <li>Nullam eu lacus auctor nunc acvcumsan tempor.</li>
  </ul>
  <div class="abs btn" style="left:137px;top:1820px;width:200px;height:48px">Read More
    <span class="arrow"><svg width="16" height="12" viewBox="0 0 16 12"><path d="M0 6h14M9 1l5 5-5 5" stroke="#fff" stroke-width="1.8" fill="none"/></svg></span>
  </div>
  <svg class="abs" style="left:634px;top:1420px" width="408" height="408" viewBox="0 0 408 408">
    <defs><radialGradient id="whyImg" cx=".45" cy=".5" r=".6"><stop offset="0" stop-color="#F090C0"/><stop offset=".5" stop-color="#F4D2E4"/><stop offset="1" stop-color="#E8EEF4"/></radialGradient></defs>
    <circle cx="204" cy="204" r="200" fill="var(--blue)"/>
    <circle cx="204" cy="204" r="192" fill="url(#whyImg)" role="img" aria-label="Illustration of a pink cell with connected molecules"/>
  </svg>

  <!-- services -->
  <div class="abs eyebrow" style="left:0;width:1200px;text-align:center;top:2034px;font-size:12px">Technology</div>
  <h2 class="abs display" style="left:0;width:1200px;text-align:center;top:2050px;font-size:45px">Our Technology Services</h2>
  <svg class="abs" style="left:572px;top:2106px" width="56" height="20" viewBox="0 0 56 20"><circle cx="10" cy="10" r="9" fill="var(--teal)"/><circle cx="30" cy="10" r="9" fill="var(--teal)"/><rect x="10" y="5" width="20" height="10" fill="var(--teal)"/><circle cx="50" cy="10" r="4" fill="var(--teal)"/></svg>

  <svg class="abs" style="left:85px;top:2150px" width="264" height="484" viewBox="0 0 264 484">
    <defs><radialGradient id="svcA" cx=".5" cy=".5" r=".6"><stop offset="0" stop-color="#E8407A"/><stop offset="1" stop-color="#142A6A"/></radialGradient></defs>
    <g fill="var(--blue)"><circle cx="132" cy="132" r="132"/><circle cx="132" cy="410" r="73"/><path d="M39,225 Q108,295 63.4,385 L200.6,385 Q156,295 225,225 Z"/></g>
    <circle cx="132" cy="132" r="118" fill="url(#svcA)" role="img" aria-label="Two glowing dividing cells"/>
    <text class="service-label" x="132" y="416" text-anchor="middle">Rapid</text>
  </svg>
  <svg class="abs" style="left:340px;top:2148px" width="264" height="484" viewBox="0 0 264 484">
    <defs><radialGradient id="svcB" cx=".5" cy=".5" r=".6"><stop offset="0" stop-color="#8AD8F0"/><stop offset="1" stop-color="#0B4C7A"/></radialGradient></defs>
    <g fill="var(--blue)"><circle cx="132" cy="352" r="132"/><circle cx="132" cy="74" r="73"/><path d="M39,259 Q108,189 63.4,99 L200.6,99 Q156,189 225,259 Z"/></g>
    <circle cx="132" cy="352" r="118" fill="url(#svcB)" role="img" aria-label="Blue microbes and particles"/>
    <text class="service-label" x="132" y="80" text-anchor="middle">Versatile</text>
  </svg>
  <svg class="abs" style="left:593px;top:2150px" width="264" height="484" viewBox="0 0 264 484">
    <defs><radialGradient id="svcC" cx=".5" cy=".5" r=".6"><stop offset="0" stop-color="#D89A5A"/><stop offset="1" stop-color="#6E5A52"/></radialGradient></defs>
    <g fill="var(--blue)"><circle cx="132" cy="132" r="132"/><circle cx="132" cy="410" r="73"/><path d="M39,225 Q108,295 63.4,385 L200.6,385 Q156,295 225,225 Z"/></g>
    <circle cx="132" cy="132" r="118" fill="url(#svcC)" role="img" aria-label="Porous orange cellular tissue"/>
    <text class="service-label" x="132" y="416" text-anchor="middle">Unbiased</text>
  </svg>
  <svg class="abs" style="left:849px;top:2148px" width="264" height="484" viewBox="0 0 264 484">
    <defs><radialGradient id="svcD" cx=".5" cy=".5" r=".6"><stop offset="0" stop-color="#4A7FE0"/><stop offset="1" stop-color="#0E1E5A"/></radialGradient></defs>
    <g fill="var(--blue)"><circle cx="132" cy="352" r="132"/><circle cx="132" cy="74" r="73"/><path d="M39,259 Q108,189 63.4,99 L200.6,99 Q156,189 225,259 Z"/></g>
    <circle cx="132" cy="352" r="118" fill="url(#svcD)" role="img" aria-label="Blue DNA double helix strand"/>
    <text class="service-label" x="132" y="80" text-anchor="middle">Inexpensive</text>
  </svg>

  <!-- testimonials -->
  <div class="abs eyebrow" style="left:85px;top:2856px;font-size:12px;color:var(--teal)">Testimonials</div>
  <h2 class="abs display section-title" style="left:85px;top:2873px">What our<br>patients saying</h2>
  <svg class="abs" style="left:85px;top:2982px" width="56" height="20" viewBox="0 0 56 20"><circle cx="10" cy="10" r="9" fill="var(--teal)"/><circle cx="30" cy="10" r="9" fill="var(--teal)"/><rect x="10" y="5" width="20" height="10" fill="var(--teal)"/><circle cx="50" cy="10" r="4" fill="var(--teal)"/></svg>
  <div class="abs circle-btn" style="left:1018px;top:2874px;border:1.5px solid var(--teal)"><svg width="20" height="12" viewBox="0 0 20 12"><path d="M20 6H2M7 1L2 6l5 5" stroke="var(--teal)" stroke-width="1.6" fill="none"/></svg></div>
  <div class="abs circle-btn" style="left:1068px;top:2874px;background:var(--teal)"><svg width="20" height="12" viewBox="0 0 20 12"><path d="M0 6h18M13 1l5 5-5 5" stroke="#fff" stroke-width="1.6" fill="none"/></svg></div>

  <div class="abs quote" style="left:85px;top:3036px">
    <div class="avatar" role="img" aria-label="Client portrait"></div>
    <div class="who"><div class="name">Noel Varga</div><div class="role">Client</div></div>
    <p>"Lorem ipslor sit amet, consectetur adipiscing elit. Nunc sollicitudin eget condimem lacinia, vestibulum et urna. Prat accumsan tincidunt nulla vitae ali. Ut at enim egestas.</p>
  </div>
  <div class="abs quote" style="left:438px;top:3036px">
    <div class="avatar" role="img" aria-label="Client portrait"></div>
    <div class="who"><div class="name">Noel Varga</div><div class="role">Client</div></div>
    <p>"Lorem ipslor sit amet, consectetur adipiscing elit. Nunc sollicitudin eget condimem lacinia, vestibulum et urna. Prat accumsan tincidunt nulla vitae ali. Ut at enim egestas.</p>
  </div>
  <div class="abs quote" style="left:790px;top:3036px">
    <div class="avatar" role="img" aria-label="Client portrait"></div>
    <div class="who"><div class="name">Noel Varga</div><div class="role">Client</div></div>
    <p>"Lorem ipslor sit amet, consectetur adipiscing elit. Nunc sollicitudin eget condimem lacinia, vestibulum et urna. Prat accumsan tincidunt nulla vitae ali. Ut at enim egestas.</p>
  </div>

  <!-- contact -->
  <svg class="abs" style="left:84px;top:3470px;overflow:visible" width="510" height="430" viewBox="0 0 510 430">
    <defs><radialGradient id="contactImg" cx=".5" cy=".5" r=".7"><stop offset="0" stop-color="#C07AE0"/><stop offset=".5" stop-color="#4A3AB0"/><stop offset="1" stop-color="#141C58"/></radialGradient></defs>
    <g fill="var(--teal)">
      <circle cx="142" cy="290" r="140"/>
      <circle cx="420" cy="90" r="90"/>
      <path d="M140.3,150 Q257.6,157.5 335,60.2 L421.1,180 Q304.4,222.5 274.2,336.3 Z"/>
    </g>
    <g role="img" aria-label="Illustration of a blue and purple DNA strand" fill="url(#contactImg)">
      <circle cx="142" cy="290" r="112"/>
      <circle cx="420" cy="90" r="62"/>
      <path d="M140.6,178 Q272.2,177.8 361.5,69.5 L420.8,152 Q289.8,202.2 247.7,327 Z"/>
    </g>
  </svg>
  <div class="abs eyebrow" style="left:616px;top:3540px;font-size:12px;color:var(--teal)">Contact Us</div>
  <h2 class="abs display section-title" style="left:616px;top:3556px">Get In Touch</h2>
  <svg class="abs" style="left:616px;top:3610px" width="56" height="20" viewBox="0 0 56 20"><circle cx="10" cy="10" r="9" fill="var(--teal)"/><circle cx="30" cy="10" r="9" fill="var(--teal)"/><rect x="10" y="5" width="20" height="10" fill="var(--teal)"/><circle cx="50" cy="10" r="4" fill="var(--teal)"/></svg>
  <div class="abs field" style="left:619px;top:3657px;width:236px">Name</div>
  <div class="abs field" style="left:877px;top:3657px;width:235px">Email</div>
  <div class="abs field" style="left:619px;top:3715px;width:236px">Phone</div>
  <div class="abs field" style="left:877px;top:3715px;width:235px">Subject</div>
  <div class="abs field" style="left:619px;top:3773px;width:493px;height:67px">Message</div>
  <div class="abs btn" style="left:619px;top:3866px;width:184px;height:46px">Submit
    <span class="arrow"><svg width="16" height="12" viewBox="0 0 16 12"><path d="M0 6h14M9 1l5 5-5 5" stroke="#fff" stroke-width="1.8" fill="none"/></svg></span>
  </div>

  <!-- footer -->
  <div class="abs brand" style="left:85px;top:4246px">
    <span class="brand-mark" style="background:#fff"></span><span class="brand-name" style="color:#fff">velquogen</span>
  </div>
  <p class="abs footer-text" style="left:82px;top:4331px;width:290px">Lorem ipsum dolor sit amet, consectetur adipiscing elit. Nunc et leo laoreet, finibus nulla in, vulputate erat. Maecenas viverra mauris non dignissim feugiat.</p>
  <div class="abs footer-head" style="left:413px;top:4348px">Contact Info</div>
  <div class="abs footer-row" style="left:413px;top:4384px;width:230px">
    <svg width="12" height="16" viewBox="0 0 12 16" style="margin-top:3px;flex:none"><path d="M6 0a6 6 0 0 1 6 6c0 4.5-6 10-6 10S0 10.5 0 6a6 6 0 0 1 6-6z" fill="var(--teal)"/><circle cx="6" cy="6" r="2.2" fill="var(--footer)"/></svg>
    <span>27 Kestrel Row, Harbourview 2040, Australia</span>
  </div>
  <div class="abs footer-head" style="left:669px;top:4348px">Get In Touch</div>
  <div class="abs footer-row" style="left:669px;top:4384px">
    <svg width="14" height="14" viewBox="0 0 24 24" style="margin-top:4px"><path fill="var(--teal)" d="M6.6 10.8a15.1 15.1 0 0 0 6.6 6.6l2.2-2.2a1 1 0 0 1 1-.25 11.4 11.4 0 0 0 3.6.57 1 1 0 0 1 1 1V20a1 1 0 0 1-1 1A17 17 0 0 1 3 4a1 1 0 0 1 1-1h3.5a1 1 0 0 1 1 1c0 1.25.2 2.45.57 3.57a1 1 0 0 1-.25 1z"/></svg>
    <span>1800-555-019</span>
  </div>
  <div class="abs footer-row" style="left:669px;top:4418px">
    <svg width="14" height="11" viewBox="0 0 24 18" style="margin-top:6px"><rect width="24" height="18" fill="var(--teal)"/><path d="M1 1l11 8 11-8" stroke="var(--footer)" stroke-width="2" fill="none"/></svg>
    <span>info@velquogen.com</span>
  </div>
  <div class="abs" style="left:865px;top:4389px;width:260px;display:flex;align-items:center;gap:12px;color:#fff;font-family:'Krona One',sans-serif;font-size:13px;white-space:nowrap">
    Follow Us <span style="width:36px;height:1px;background:#fff;opacity:.6"></span>
    <span style="display:flex;gap:22px"><span class="social-dot" style="margin:0"></span><span class="social-dot" style="margin:0"></span><span class="social-dot" style="margin:0"></span><span class="social-dot" style="margin:0"></span></span>
  </div>
  <div class="abs" style="left:85px;top:4518px;width:1030px;height:1px;background:#3A464C"></div>
  <div class="abs legal">
    <div class="links"><span class="on">Home</span><span>|</span><span>About Us</span><span>|</span><span>Technology</span><span>|</span><span>Contact Us</span></div>
    <div style="margin-left:95px">© 2025 <span style="color:var(--teal)">VELQUOgen</span>. All right reserved.</div>
  </div>

</div>
</body>
</html>
```